Soy Candle Labels

We sell soy candles in recycled wine bottles. The wine bottle is cut in half and filled with pure and natural soy wax and scented with essential oils.
Our product represents good use of up cycling materials for a better use. The product is all natural and eco friendly.
You can see good use of labels and branding for a company in America that does the same thing http://marrowlanewicks.example/
Trya dn keep the label uncomplicated like the above labels.
We will need an area to hand stamp the scent. Similar to the labels used on the above website.
We would prefer to use a white or off white paper label with gold or bronze printing - limit the use of colour and keep the label simple and sophisticated.
Brambrel Candle Co. is our company name. Brambrel being the predominant name and candle co. written small underneath right justified.
Die cut labels might look better than a rectangle.
Dimensions should be 90mm Wide x 90mm High
The final design should communicate a professional and quality product. But stay modern and professional. Clean, elegant and sophisticated.
Can use wording such as: Hand Poured, Premium Soy Wax, All Natural, Up cycled
Have a look at the attached image for the look and feel we are going for.
Updates
Designers are having a little bit of trouble interpreting the brief into a viable design. To assist perhaps you can look at WINE LABELS on google images. Design your label around an existing style wine label to give the canld ethe feel of being a bottle of wine. Get creative! :)
Reason: We require more designs. We havnt quite got what were looking for.
Please see brief.

```html
<!DOCTYPE html>
<html lang="en">
<head>
<meta charset="utf-8">
<title>Brambrel Candle Co. – Soy Candle Label</title>
<link rel="stylesheet" href="https://fonts.googleapis.com/css2?family=Fira+Sans:wght@400&family=Pathway+Gothic+One&display=swap">
<style>
  :root {
    --backdrop: #3a1c10;
    --paper: #fdfcf5;
    --ink: #3a1c10;
  }
  html, body {
    margin: 0;
    padding: 0;
    width: 1200px;
    height: 1000px;
    overflow: hidden;
    background: var(--backdrop);
  }
  .canvas {
    position: relative;
    width: 1200px;
    height: 1000px;
    background: var(--backdrop);
  }
  .label {
    position: absolute;
    left: 151px;
    top: 70px;
    width: 875px;
    height: 874px;
    background: var(--paper);
    border-radius: 22px;
    color: var(--ink);
    font-family: "Fira Sans", "Helvetica Neue", Arial, sans-serif;
  }
  .label-frame {
    position: absolute;
    left: 15px;
    top: 15px;
    right: 15px;
    bottom: 15px;
    border: 1.5px solid var(--ink);
    border-radius: 18px;
  }
  .claims {
    position: absolute;
    left: 44px;
    top: 38px;
    margin: 0;
    line-height: 1;
  }
  .claims-title {
    display: block;
    font-size: 38px;
    margin-bottom: 12px;
  }
  .claims-line {
    display: block;
    font-size: 27px;
    margin-bottom: 9px;
  }
  .claims-line.small { font-size: 25px; }
  .brand {
    position: absolute;
    left: 150px;
    top: 390px;
    width: 680px;
    text-align: right;
    line-height: 1;
  }
  .brand-name {
    display: block;
    font-size: 138px;
    font-weight: 400;
    letter-spacing: 1px;
  }
  .brand-sub {
    display: block;
    font-size: 32px;
    font-weight: 400;
    margin-top: 8px;
    margin-right: 48px;
  }
  .footer-note {
    position: absolute;
    top: 766px;
    font-family: "Pathway Gothic One", "Arial Narrow", sans-serif;
    font-size: 46px;
    line-height: 1;
    display: flex;
    align-items: center;
    gap: 16px;
  }
  .footer-note.origin { left: 45px; }
  .footer-note.material { right: 42px; }
  .scroll-ornament {
    display: block;
    width: 62px;
    height: 52px;
    background: linear-gradient(90deg, rgba(58,28,16,0.18), rgba(58,28,16,0.32));
    border-radius: 4px;
  }
</style>
</head>
<body>
  <main class="canvas">
    <section class="label">
      <div class="label-frame"></div>

      <p class="claims">
        <span class="claims-title">Hand Poured</span>
        <span class="claims-line">All Natural Soy</span>
        <span class="claims-line small">320 gm of Premium Soy Wax</span>
      </p>

      <h1 class="brand">
        <span class="brand-name">Brambrel</span>
        <span class="brand-sub">Candle Co.</span>
      </h1>

      <div class="footer-note origin">
        <span>Product of Australia</span>
        <span class="scroll-ornament" role="img" aria-label="Small decorative scroll flourish"></span>
      </div>

      <div class="footer-note material">
        <span class="scroll-ornament" role="img" aria-label="Small decorative scroll flourish"></span>
        <span>up-cycled wine bottle</span>
      </div>
    </section>
  </main>
</body>
</html>
```